Flyer for American Indian Elders on Dementia Warning Signs

We need a flyer designed for older adults who are American Indian or Alaska Native (in the U.S.).

Ideally, the flyer should complement the colors of our logos. The project logo and our organization logo are attached to the brief.

When people see the flyer we want them to feel that it represents their culture, is warm, and professional but relatable to older adults and people who have limited incomes.

I have attached an earlier draft of the document we designed ourselves BUT we want different and better.

It is for older adults who have trouble reading so:
1. you must use a font that is 11.5 points or larger
2. Do not put text over complex pictures or use shading with words
3. You can use a serif font for the heading, but should use san serif for the body text
4. There should be good contrast between the font color and background

Please do not use any images that include a head dress or pictures of American Indian people or things that are very traditional or "token" imagery.

We need to save a small space under the call out box/ somewhere on the flyer for other people to add their logo once they download.

Let us know if you have questions or need additional information.

Target Market(s)

Older American Indian people

Font styles to use
Serif
Sans Serif

Requirements
Must have
• Easy to read for older adults
Should not have
• indian headdress

```html
<!DOCTYPE html>
<html lang="en">
<head>
<meta charset="utf-8">
<title>10 Signs of Thinking or Memory Changes that Might be Dementia</title>
<link href="https://fonts.googleapis.com/css2?family=Roboto:wght@400;700;900&display=swap" rel="stylesheet">
<style>
  :root {
    --teal: #4fa9b3;
    --clay: #9b504a;
    --clay-dark: #7d3735;
    --ink: #111111;
    --white: #ffffff;
  }
  * { margin: 0; padding: 0; box-sizing: border-box; }
  html, body { width: 848px; height: 1200px; overflow: hidden; background: var(--white); }
  body { font-family: "Roboto", Arial, sans-serif; color: var(--ink); }
  .flyer { position: relative; width: 848px; height: 1200px; overflow: hidden; background: var(--white); }

  .hero { position: absolute; left: 0; top: 0; width: 848px; height: 300px; }
  .hero-title {
    position: absolute; left: 0; width: 848px; top: 40px;
    text-align: center; color: var(--white);
    font-weight: 900; font-size: 37px; line-height: 44px; letter-spacing: 0.2px;
  }

  .signs { position: absolute; left: 0; top: 0; }
  .sign { position: absolute; left: 26px; width: 660px; }
  .sign-num {
    position: absolute; left: 0; top: -5px; width: 34px; height: 34px; border-radius: 50%;
    background: var(--teal); color: var(--white);
    font-weight: 700; font-size: 16px; line-height: 34px; text-align: center;
  }
  .sign-body { margin-left: 40px; font-size: 17px; line-height: 20.5px; }
  .sign-title { font-weight: 700; font-size: 17px; }
  .sign-list { list-style: none; margin-top: 6px; font-size: 16.3px; line-height: 19.5px; }

  .callout {
    position: absolute; left: 505px; top: 286px; width: 343px; height: 567px;
    background: var(--clay); border-top-left-radius: 54px; overflow: hidden;
  }
  .callout-text {
    padding: 48px 36px 0 40px; color: var(--white); text-align: center;
    font-size: 19.5px; line-height: 24px;
  }
  .callout-text p + p { margin-top: 24px; }
  .callout-text strong { font-weight: 700; }
  .partner-band {
    position: absolute; left: 0; bottom: 0; width: 100%; height: 109px;
    background: var(--clay-dark); display: flex; align-items: center; justify-content: center; gap: 12px;
  }
  .partner-mark { width: 56px; height: 56px; border-radius: 50%; border: 3px solid var(--white); flex: none; }
  .partner-name { color: var(--white); font-weight: 700; font-size: 15px; line-height: 18px; text-transform: uppercase; width: 170px; }

  .footer { position: absolute; left: 0; top: 1142px; width: 848px; height: 58px; }
  .footer-band { position: absolute; left: 0; top: 0; }
  .org { position: absolute; left: 43px; top: 8px; display: flex; align-items: center; gap: 14px; }
  .org-mark { width: 42px; height: 42px; background: var(--teal); flex: none; }
  .org-name { color: var(--clay); font-weight: 700; font-size: 15px; line-height: 17px; text-transform: uppercase; width: 180px; }
  .links { position: absolute; left: 385px; top: 19px; color: var(--white); font-size: 16px; line-height: 20px; white-space: nowrap; }
  .links .sep { margin: 0 10px; }
</style>
</head>
<body>
<div class="flyer">

  <svg class="hero" viewBox="0 0 848 300" width="848" height="300">
    <defs>
      <linearGradient id="landscape" x1="0" y1="0" x2="0" y2="1">
        <stop offset="0" stop-color="#3c4349"/>
        <stop offset="0.35" stop-color="#6f6b66"/>
        <stop offset="0.55" stop-color="#8a4a2c"/>
        <stop offset="1" stop-color="#a8673f"/>
      </linearGradient>
    </defs>
    <path role="img" aria-label="Photo of desert mesas under a stormy sky"
      fill="url(#landscape)"
      d="M0 0 H848 V115 C800 190 740 225 679 219 C610 212 560 150 512 152 C470 155 420 240 380 275 C360 292 330 290 313 272 C270 225 250 180 209 178 C150 176 110 185 78 180 C40 175 15 150 0 131 Z"/>
    <path fill="none" stroke="var(--teal)" stroke-width="6"
      d="M0 131 C15 150 40 175 78 180 C110 185 150 176 209 178 C250 180 270 225 313 272 C330 290 360 292 380 275 C420 240 470 155 512 152 C560 150 610 212 679 219 C740 225 800 190 848 115"/>
  </svg>
  <h1 class="hero-title">10 Signs of Thinking or Memory<br>Changes that Might be Dementia</h1>

  <section class="signs">
    <div class="sign" style="top:314px">
      <span class="sign-num">01</span>
      <div class="sign-body">
        <div class="sign-title">Memory loss that affects your daily life. You may:</div>
        <ul class="sign-list">
          <li>Forget events or important dates</li>
          <li>Repeat yourself</li>
          <li>Rely more often on lists or sticky notes to remember things</li>
        </ul>
      </div>
    </div>

    <div class="sign" style="top:412px">
      <span class="sign-num">02</span>
      <div class="sign-body">
        <div class="sign-title">Trouble planning or solving problems. You may<br>have a harder time:</div>
        <ul class="sign-list">
          <li>Paying bills</li>
          <li>Cooking recipes you have used for years</li>
        </ul>
      </div>
    </div>

    <div class="sign" style="top:515px">
      <span class="sign-num">03</span>
      <div class="sign-body">
        <div class="sign-title">Get confused about the time, date, or where you are.</div>
      </div>
    </div>

    <div class="sign" style="top:556px">
      <span class="sign-num">04</span>
      <div class="sign-body">
        <div><span class="sign-title">Daily tasks are getting harder,</span> including:</div>
        <ul class="sign-list">
          <li>Driving</li>
          <li>Making a grocery list or going shopping</li>
        </ul>
      </div>
    </div>

    <div class="sign" style="top:632px">
      <span class="sign-num">05</span>
      <div class="sign-body">
        <div><span class="sign-title">Trouble with how your eyesight and thinking work<br>together that gets worse.</span> This includes:</div>
        <ul class="sign-list">
          <li>Tripping, falls, or problems with your balance</li>
          <li>Spilling or dropping things more</li>
        </ul>
      </div>
    </div>

    <div class="sign" style="top:728px">
      <span class="sign-num">06</span>
      <div class="sign-body">
        <div><span class="sign-title">New trouble talking or writing.</span> You have a hard time<br>finding the words you want to say. For example, you<br>may say “that thing on your wrist that tells time”<br>instead of “watch.”</div>
      </div>
    </div>

    <div class="sign" style="top:820px">
      <span class="sign-num">07</span>
      <div class="sign-body">
        <div><span class="sign-title">Lose and cannot find things.</span> For example, you:</div>
        <ul class="sign-list">
          <li>Can’t find the coffee pot that you use every day</li>
          <li>Might put your car keys in the freezer</li>
        </ul>
      </div>
    </div>

    <div class="sign" style="top:892px">
      <span class="sign-num">08</span>
      <div class="sign-body">
        <div><span class="sign-title">Notice changes in mood or personality,</span> such as being:</div>
        <ul class="sign-list">
          <li>Easily mad or sad in everyday situations</li>
          <li>More fearful (scared) or suspicious (not trusting)</li>
        </ul>
      </div>
    </div>

    <div class="sign" style="top:976px">
      <span class="sign-num">09</span>
      <div class="sign-body">
        <div><span class="sign-title">Act different and make poor choices.</span> This may make you more likely to:</div>
        <ul class="sign-list">
          <li>Spend money you do not have or be a scam victim</li>
          <li>Stop washing up regularly or pay less attention to how you look</li>
          <li>Forget to take care of your pet</li>
        </ul>
      </div>
    </div>

    <div class="sign" style="top:1076px; width:720px">
      <span class="sign-num">10</span>
      <div class="sign-body">
        <div><span class="sign-title">Pull away from friends and family because it is harder to keep up.</span> You may not<br>want to do things you used to enjoy, like sporting events, church, music, or sex.</div>
      </div>
    </div>
  </section>

  <aside class="callout">
    <div class="callout-text">
      <p>As we get older, we may slow down a bit. This is a normal part of aging. <strong>Changes in memory or thinking</strong> that make it harder to get through the day, are not a normal part of aging. These may be early signs of dementia.</p>
      <p>Because American Indian and Alaska Native people have a high risk of dementia, it is important to know the warning signs. <strong>Do you have any of these 10 signs? If so, talk to your doctor.</strong></p>
    </div>
    <div class="partner-band">
      <span class="partner-mark"></span>
      <span class="partner-name">Red Mesa Brain Wellness Center</span>
    </div>
  </aside>

  <footer class="footer">
    <svg class="footer-band" viewBox="0 0 848 58" width="848" height="58">
      <path fill="var(--teal)" d="M345 0 H848 V58 H323 Z"/>
    </svg>
    <div class="org">
      <span class="org-mark"></span>
      <span class="org-name">Circle of Elders Alliance</span>
    </div>
    <div class="links">www.RedMesaWellness.org<span class="sep">|</span>www.elderhub.org/aging</div>
  </footer>

</div>
</body>
</html>
```